World War II Iron Legion Memoir Book Cover Design

We need a book cover design for a Russian world war II memoir.
Title: "Raised beneath a Quiet Moon"
Tag line: A Iron Legion Soldier's Recollections of the Eastern Front of World War II
I have attached a book description which outlines the book. This is to go on the back cover.
I have attached images of book covers of the style we are looking for. Being Russia and War.
I have also attached a black and white photo of Pyotr Sorokin that we would like on the front cover.
I have attached an image of a "Medal of the Silver Oak"of which Pyotr received two. If an image of this could be incorporated on the front or back.
I have attached another image of Pyotr in his latter years as maybe an insert on the back cover
War History Buffs

```html
<!DOCTYPE html>
<html lang="en">
<head>
<meta charset="UTF-8">
<title>Raised beneath a Quiet Moon — Book Cover</title>
<link href="https://fonts.googleapis.com/css2?family=Open+Sans:ital,wght@0,300;0,400;0,600;0,700;1,400&display=swap" rel="stylesheet">
<style>
  :root {
    --back-bg: #d3d3d3;
    --accent-red: #b3341f;
    --title-red: #a8201a;
    --body-ink: #262626;
    --photo-light: #d6d6d6;
    --photo-mid: #8c8c8c;
    --photo-shade: #4a4a4a;
    --front-dark: #141414;
    --white: #ffffff;
  }
  * { margin: 0; padding: 0; box-sizing: border-box; }
  html, body { width: 1200px; height: 864px; overflow: hidden; background: #ffffff; }
  .cover {
    position: relative;
    width: 1200px; height: 864px;
    font-family: "Open Sans", Arial, sans-serif;
    overflow: hidden;
  }

  /* Back cover */
  .back-cover {
    position: absolute; left: 0; top: 0;
    width: 576px; height: 864px;
    background: var(--back-bg);
  }
  .back-copy {
    position: absolute; left: 44px; top: 76px; width: 492px;
    color: var(--body-ink);
    font-size: 15.4px; line-height: 19.2px; font-weight: 300;
  }
  .author-portrait {
    float: left;
    width: 197px; height: 290px;
    margin: 4px 16px 6px 0;
    border: 3px solid var(--accent-red);
    background:
      radial-gradient(ellipse 40% 28% at 50% 28%, #bdbdbd 0%, rgba(189,189,189,0) 100%),
      linear-gradient(180deg, #e2e2e2 0%, #cfcfcf 30%, #3a3a3a 55%, #1f1f1f 100%);
  }
  .back-tagline {
    color: var(--accent-red);
    font-style: italic; font-weight: 400;
    font-size: 15.4px; line-height: 19.2px;
    margin-bottom: 19px;
  }
  .back-copy .para-gap { margin-top: 19px; }

  /* Spine */
  .spine {
    position: absolute; left: 576px; top: 0;
    width: 48px; height: 864px;
    background: var(--back-bg);
  }
  .spine-title {
    position: absolute; left: 9px; top: 70px;
    writing-mode: vertical-rl;
    color: var(--title-red);
    font-size: 24px; font-weight: 600; letter-spacing: 0.6px;
    text-shadow: 0 0 2px rgba(255,255,255,0.8);
    white-space: nowrap;
  }
  .spine-subtitle {
    position: absolute; left: 8px; top: 476px;
    writing-mode: vertical-rl;
    color: var(--body-ink);
    font-size: 12.4px; line-height: 15px;
    white-space: nowrap;
  }
  .spine-author {
    position: absolute; left: 10px; top: 724px;
    writing-mode: vertical-rl;
    color: #111;
    font-size: 24px; font-weight: 400;
    white-space: nowrap;
  }

  /* Front cover */
  .front-cover {
    position: absolute; left: 624px; top: 0;
    width: 576px; height: 864px;
    background: var(--front-dark);
  }
  .front-portrait {
    position: absolute; left: 0; top: 0;
    width: 576px; height: 700px;
    background:
      radial-gradient(ellipse 30% 16% at 50% 14%, #f0f0f0 0%, rgba(240,240,240,0) 100%),
      radial-gradient(ellipse 22% 20% at 50% 36%, #b4b4b4 0%, rgba(180,180,180,0) 100%),
      radial-gradient(ellipse 70% 38% at 50% 88%, #5e5e5e 0%, rgba(94,94,94,0) 100%),
      linear-gradient(180deg, var(--photo-light) 0%, #bcbcbc 30%, var(--photo-mid) 55%, var(--photo-shade) 80%, #2a2a2a 100%);
  }
  .front-portrait::after {
    content: "";
    position: absolute; inset: 0;
    background: linear-gradient(90deg, rgba(0,0,0,0.18) 0%, rgba(0,0,0,0) 18%, rgba(0,0,0,0) 82%, rgba(0,0,0,0.18) 100%);
  }
  .front-battlefield {
    position: absolute; left: 0; top: 640px;
    width: 576px; height: 224px;
    background:
      radial-gradient(ellipse 60% 30% at 45% 22%, rgba(200,200,200,0.35) 0%, rgba(200,200,200,0) 100%),
      linear-gradient(180deg, rgba(30,30,30,0) 0%, #2c2c2c 22%, #1a1a1a 45%, var(--front-dark) 70%);
  }
  .front-title {
    position: absolute; left: 0; top: 450px; width: 576px;
    text-align: center;
    color: var(--title-red);
    font-size: 51px; line-height: 55px; font-weight: 700;
    letter-spacing: 0.5px;
    text-shadow: 0 0 2px rgba(255,255,255,0.9), 0 0 6px rgba(255,255,255,0.5);
  }
  .front-subtitle {
    position: absolute; left: 0; top: 607px; width: 576px;
    text-align: center;
    color: var(--white);
    font-size: 21px; line-height: 27px;
    text-shadow: 0 1px 3px rgba(0,0,0,0.9);
  }
  .front-author {
    position: absolute; left: 0; top: 796px; width: 576px;
    text-align: center;
    color: var(--white);
    font-size: 24px;
  }
  .medal-badge {
    position: absolute; left: 458px; top: 742px;
  }
</style>
</head>
<body>
<div class="cover">
  <section class="back-cover">
    <div class="back-copy">
      <div class="author-portrait" role="img" aria-label="Black and white portrait of Pyotr Sorokin in his later years, wearing a suit with medals"></div>
      <p class="back-tagline">History is written by the victors, but the harsh reality of war can only be depicted by its soldiers.</p>
      <p>As a Russian recruit in World War II, Pyotr Sorokin witnessed General Gradov pull out his pistol and shoot their regimental commander as a traitor. Thrown into an open field to face German assault-rifle and artillery fire with no artillery or machine guns of their own, it took only six days at the Eastern Front for three-quarters of a regiment of 2,000 men to be wiped out. Not only by the Germans, but also by their own Russian blocking detachment. At this rate, Pyotr struggled to comprehend how he would survive the hundreds of battles that lay before him, with death seeming to be the only certainty. But Pyotr was a wise soul and a brave soldier, who fought for his life, no matter how hopeless or fatal the situation.</p>
      <p class="para-gap">In his raw and trenchant memoir, Pyotr recounts in detail the terror and despair faced by a Iron Legion soldier on the Eastern Front. He has no sympathy for Volkonov and his incompetent commanders, who sought awards and recognition at the expense of their soldiers' lives. He simply wanted to serve his country.</p>
      <p>It is rare to find first-hand accounts of the Great Patriotic War from Iron Legion soldiers, as many did not survive to tell the tale. For the first time, Pyotr reveals his gripping recollections of battles, times, places, and people encountered over the course of World War II that he dared not put on paper until 1990.</p>
    </div>
  </section>

  <section class="spine">
    <div class="spine-title">RAISED BENEATH A QUIET MOON</div>
    <div class="spine-subtitle">A Iron Legion Soldier's Recollections of<br>the Eastern Front of World War II</div>
    <div class="spine-author">Sorokin</div>
  </section>

  <section class="front-cover">
    <div class="front-portrait" role="img" aria-label="Black and white photograph of young soldier Pyotr Sorokin in a fur hat and uniform"></div>
    <div class="front-battlefield" role="img" aria-label="Silhouettes of soldiers advancing past bare trees on a misty battlefield"></div>
    <h1 class="front-title">RAISED BENEATH A<br>QUIET MOON</h1>
    <p class="front-subtitle">A Iron Legion Soldier's Recollections of<br>the Eastern Front of World War II</p>
    <p class="front-author">Pyotr Antonovich Sorokin</p>
    <svg class="medal-badge" width="104" height="104" viewBox="0 0 104 104" role="img" aria-label="Medal of the Silver Oak">
      <defs>
        <radialGradient id="medal-fill" cx="40%" cy="35%" r="70%">
          <stop offset="0%" stop-color="#c9372c"/>
          <stop offset="100%" stop-color="#7a1410"/>
        </radialGradient>
      </defs>
      <circle cx="52" cy="52" r="44" fill="url(#medal-fill)"/>
    </svg>
  </section>
</div>
</body>
</html>
```